RoadReady Driving School

I need a Facebook page for my Driving School. I teach mostly teenagers how to drive in New Hampshire but also do private classes for adults as well. More info can be found at roadreadylessons.example

```html
<!DOCTYPE html>
<html lang="en">
<head>
<meta charset="utf-8">
<title>RoadReady Driving School – Facebook Cover</title>
<link rel="stylesheet" href="https://fonts.googleapis.com/css2?family=Exo+2:ital,wght@0,700;1,700&family=Poppins:wght@600;700&display=swap">
<style>
  :root {
    --page: #ffffff;
    --asphalt: #1f1f1f;
    --photo-dark: #0c0c0c;
    --photo-mid: #4a4a4a;
    --photo-light: #9a9a9a;
    --brand-yellow: #f0c20c;
    --ink-white: #ffffff;
    --tick-ink: #1f1f1f;
  }
  * { box-sizing: border-box; margin: 0; padding: 0; }
  html, body {
    width: 1200px;
    height: 824px;
    overflow: hidden;
    background: var(--page);
  }
  .cover {
    position: absolute;
    left: 77px;
    top: 212px;
    width: 1046px;
    height: 386px;
    background: var(--asphalt);
    overflow: hidden;
  }
  .cover-art {
    position: absolute;
    inset: 0;
    width: 1046px;
    height: 386px;
  }
  .brand {
    position: absolute;
    left: 49px;
    top: 46px;
    display: flex;
    align-items: center;
    gap: 14px;
  }
  .brand-dot {
    width: 52px;
    height: 52px;
    border-radius: 50%;
    background: var(--brand-yellow);
    flex: none;
  }
  .brand-name {
    font-family: "Poppins", sans-serif;
    font-weight: 700;
    font-size: 26px;
    line-height: 1.1;
    color: var(--ink-white);
    white-space: nowrap;
  }
  .brand-phone {
    position: absolute;
    left: 115px;
    top: 110px;
    font-family: "Poppins", sans-serif;
    font-weight: 700;
    font-size: 15px;
    letter-spacing: 1px;
    color: var(--ink-white);
  }
  .services {
    position: absolute;
    left: 51px;
    top: 162px;
    list-style: none;
  }
  .service {
    display: flex;
    align-items: center;
    gap: 12px;
    height: 42px;
    font-family: "Poppins", sans-serif;
    font-weight: 600;
    font-size: 26px;
    color: var(--ink-white);
  }
  .service-tick { width: 24px; height: 24px; flex: none; }
  .headline {
    position: absolute;
    left: 586px;
    top: 50px;
    width: 410px;
    height: 170px;
    overflow: visible;
  }
  .headline-word {
    font-family: "Exo 2", sans-serif;
    font-weight: 700;
    fill: var(--ink-white);
  }
  .headline-place {
    font-family: "Exo 2", sans-serif;
    font-style: italic;
    font-weight: 700;
    fill: var(--brand-yellow);
  }
</style>
</head>
<body>
  <section class="cover">
    <svg class="cover-art" viewBox="0 0 1046 386">
      <defs>
        <linearGradient id="bridgeTones" x1="0" y1="0" x2="0" y2="1">
          <stop offset="0" stop-color="var(--photo-dark)"/>
          <stop offset="0.55" stop-color="var(--photo-mid)"/>
          <stop offset="0.8" stop-color="var(--photo-light)"/>
          <stop offset="1" stop-color="var(--photo-mid)"/>
        </linearGradient>
      </defs>
      <path role="img" aria-label="Night photograph of a road leading across a lit steel bridge"
            d="M400,0 C470,180 700,312 1046,286 L1046,0 Z" fill="url(#bridgeTones)"/>
      <path class="swoosh" d="M392,0 C455,205 690,352 1046,328 L1046,286 C700,312 470,180 402,0 Z"
            fill="var(--brand-yellow)"/>
    </svg>

    <div class="brand">
      <span class="brand-dot"></span>
      <span class="brand-name">RoadReady<br>Driving School</span>
    </div>
    <div class="brand-phone">603 555 0142</div>

    <ul class="services">
      <li class="service">
        <svg class="service-tick" viewBox="0 0 24 24" aria-hidden="true">
          <circle cx="12" cy="12" r="11" fill="var(--brand-yellow)"/>
          <path d="M6.5 12.5 L10.5 16.5 L17.5 7.5" fill="none" stroke="var(--tick-ink)" stroke-width="3" stroke-linecap="round" stroke-linejoin="round"/>
        </svg>
        Teenage driving lesson
      </li>
      <li class="service">
        <svg class="service-tick" viewBox="0 0 24 24" aria-hidden="true">
          <circle cx="12" cy="12" r="11" fill="var(--brand-yellow)"/>
          <path d="M6.5 12.5 L10.5 16.5 L17.5 7.5" fill="none" stroke="var(--tick-ink)" stroke-width="3" stroke-linecap="round" stroke-linejoin="round"/>
        </svg>
        Private classes for adults
      </li>
    </ul>

    <svg class="headline" viewBox="0 0 410 170" role="heading" aria-level="1">
      <text class="headline-word" x="3" y="63" font-size="70" textLength="402" lengthAdjust="spacingAndGlyphs">DRIVING</text>
      <text class="headline-word" x="3" y="126" font-size="70" textLength="402" lengthAdjust="spacingAndGlyphs">LESSON</text>
      <text class="headline-place" x="0" y="158" font-size="28" textLength="408" lengthAdjust="spacingAndGlyphs">IN NEW HAMPSHIRE</text>
    </svg>
  </section>
</body>
</html>
```